Bright Tail Botanicals: Extracts for Pets

We need a brochure to help market the products. Bright Tail Botanicals makes Chinese Herbal Extracts for cats and dogs. We have three products to launch with. An allergy, calming, and pain formula. They are based on traditional Chinese Medicine Formulas that have been used for hundreds of years on humans and animals. I would like the logo (attached) and have one or two cat/dogs pictures. They can be any of the pics from my website. Each product should have a descrition of what it treats (can pull from website). The brochure can highlight its convient, effective, and a safe alternative. It has to include:

This statement has not been evaluated by the FDA.
This product is not intended to diagnose, treat, cure,
or prevent any disease. Bright Tail is not liable for any adverse effects.

I included a sample with some of the important info for the products - the desing does not have to be similar, just an example of the copy

*I would like the format to be in Illustrator, vector, so that I can change sizes if I need to without loosing any detail.

Target Market(s)

Pet Owners

Industry/Entity Type

Pet Care

Font styles to use
Other font styles liked:
• Universal (as logo)

Requirements
Must have
• Logo, Description of each products.
Nice to have
• Dog or cat picture

```html
<!DOCTYPE html>
<html lang="en">
<head>
<meta charset="UTF-8">
<title>Bright Tail Botanicals – Pet Care</title>
<link href="https://fonts.googleapis.com/css2?family=Lato:wght@400;700&display=swap" rel="stylesheet">
<style>
  :root {
    --lime: #b6cf44;
    --leaf: #7fbf3f;
    --forest: #4b7d3a;
    --ink: #4a4a4a;
    --white: #ffffff;
    --paper: #ffffff;
    --photo-light: #f6f1ea;
    --photo-warm: #d9c2a3;
  }
  html, body {
    margin: 0;
    padding: 0;
    overflow: hidden;
    background: var(--paper);
  }
  .flyer {
    position: relative;
    width: 848px;
    height: 1200px;
    overflow: hidden;
    background: var(--paper);
    font-family: "Lato", sans-serif;
    color: var(--white);
  }
  .backdrop {
    position: absolute;
    inset: 0;
  }
  .tag {
    position: absolute;
    left: 0;
    top: 104px;
    width: 448px;
    height: 96px;
    background: var(--lime);
    box-shadow: 2px 2px 3px rgba(0,0,0,0.2);
  }
  .tag-text {
    position: absolute;
    left: 34px;
    top: 16px;
    margin: 0;
    font-size: 58px;
    font-weight: 700;
    letter-spacing: -2px;
    line-height: 64px;
  }
  .brand {
    position: absolute;
    left: 520px;
    top: 76px;
    width: 230px;
    text-align: center;
  }
  .brand-mark {
    width: 150px;
    height: 150px;
    margin: 0 auto 26px;
    border-radius: 50%;
    background: var(--leaf);
  }
  .brand-name {
    margin: 0;
    font-size: 36px;
    font-weight: 400;
    line-height: 42px;
    color: var(--forest);
  }
  .headline {
    position: absolute;
    left: 32px;
    top: 350px;
    margin: 0;
    font-size: 66px;
    font-weight: 400;
    line-height: 80px;
  }
  .photo {
    position: absolute;
    left: 40px;
    top: 690px;
    width: 768px;
    height: 240px;
    background: linear-gradient(180deg, var(--photo-light) 0%, var(--photo-warm) 100%);
    border-radius: 6px;
  }
  .badge {
    position: absolute;
    left: 595px;
    top: 641px;
    width: 206px;
    height: 206px;
    border-radius: 50%;
    background: var(--leaf);
  }
  .badge-inner {
    position: absolute;
    inset: 12px;
    border-radius: 50%;
    background: var(--lime);
    display: flex;
    align-items: center;
    justify-content: center;
    text-align: center;
    font-size: 43px;
    line-height: 46px;
  }
  .products {
    position: absolute;
    left: 40px;
    top: 946px;
    width: 768px;
    display: flex;
    gap: 24px;
  }
  .product {
    flex: 1;
    border-top: 4px solid var(--leaf);
    padding-top: 8px;
  }
  .product-name {
    margin: 0 0 4px;
    font-size: 20px;
    font-weight: 700;
    color: var(--forest);
  }
  .product-text {
    margin: 0;
    font-size: 14px;
    line-height: 19px;
    color: var(--ink);
  }
  .disclaimer {
    position: absolute;
    left: 40px;
    top: 1078px;
    width: 768px;
    margin: 0;
    font-size: 11.5px;
    line-height: 15px;
    text-align: center;
    color: var(--ink);
  }
  .footer {
    position: absolute;
    left: 0;
    top: 1134px;
    width: 848px;
    height: 53px;
    background: var(--lime);
    border-bottom: 13px solid var(--leaf);
    display: flex;
    align-items: center;
    justify-content: center;
    font-size: 20px;
  }
  .footer-label {
    font-size: 15px;
    margin-right: 8px;
  }
</style>
</head>
<body>
<main class="flyer">
  <svg class="backdrop" width="848" height="1200" viewBox="0 0 848 1200" aria-hidden="true">
    <polygon points="0,236 848,535 848,623 0,623" fill="var(--leaf)"/>
    <polygon points="0,254 848,551 848,623 0,623" fill="var(--lime)"/>
  </svg>

  <div class="tag"><h2 class="tag-text">PET CARE</h2></div>

  <div class="brand">
    <div class="brand-mark"></div>
    <p class="brand-name">Bright Tail<br>Botanicals</p>
  </div>

  <h1 class="headline">TAKE<br>A GOOD<br>CARE OF PETS</h1>

  <div class="photo" role="img" aria-label="Photo of kittens and puppies sitting in a row on a white background"></div>

  <div class="badge"><div class="badge-inner">100%<br>CARE</div></div>

  <section class="products">
    <article class="product">
      <h3 class="product-name">Allergy Formula</h3>
      <p class="product-text">Soothes itchy skin, sneezing and seasonal allergies in cats and dogs.</p>
    </article>
    <article class="product">
      <h3 class="product-name">Calming Formula</h3>
      <p class="product-text">Eases anxiety, noise fears and travel stress the natural way.</p>
    </article>
    <article class="product">
      <h3 class="product-name">Pain Formula</h3>
      <p class="product-text">Supports joint comfort and easy movement for aging or active pets.</p>
    </article>
  </section>

  <p class="disclaimer">This statement has not been evaluated by the FDA. This product is not intended to diagnose, treat, cure,<br>or prevent any disease. Bright Tail is not liable for any adverse effects.</p>

  <footer class="footer"><span class="footer-label">WEBSITE:</span> www.yoursitename.com</footer>
</main>
</body>
</html>
```